IT company requires website redesign

I have an old boring website that I want to update - www.tvkb-example.net
I am a growing IT company beginning to look after more healthcare professionals such as medical and dental practices so a more professional look is required

Blue and orange are the company colours. See one of our local competitors for your reference and ideas - https://www.plinth-halvard.example.au

Target Market(s)

Medical, dental, professional, solicitors etc

Industry/Entity Type

It Support

Number of Pages Required

5+ page

Colors

Designer to choose colors to be used in the design.

Requirements
Must have
• Classy feel, simple with the 'less is more' approach
• On support page, links to support items, a couple more to come
• Reference to our technology partners
• Easy to read
Nice to have
• Company colours are blue with a little orange but I willing to consider new web colour schemes
• leave the rest to you

```html
<!DOCTYPE html>
<html lang="en">
<head>
<meta charset="utf-8">
<title>Corelink Systems — IT Support</title>
<link href="https://fonts.googleapis.com/css2?family=Lato:wght@300;400;700;900&family=Montserrat:wght@400;600;700&display=swap" rel="stylesheet">
<style>
:root{
  --blue:#3f63c9;
  --blue-band:#2f6aad;
  --blue-help:#5a7ef0;
  --navy:#2d2e4a;
  --phone:#363c78;
  --orange:#f07a3b;
  --ink:#333a4d;
  --muted:#8a8fa0;
  --line:#d9dce4;
  --white:#ffffff;
}
*{box-sizing:border-box;margin:0;padding:0}
html,body{width:1200px;height:4952px;overflow:hidden}
body{position:relative;background:var(--white);font-family:"Lato",sans-serif;color:var(--ink)}
.abs{position:absolute}
/* hero */
.hero{left:0;top:0;width:1200px;height:628px;background:linear-gradient(135deg,#a77d56 0%,#c89f74 35%,#dfe6ee 55%,#9fb4c8 100%)}
.hero-screen{left:300px;top:60px;width:600px;height:420px;border-radius:24px;background:linear-gradient(180deg,#f6f7fa,#e4e8ef);box-shadow:0 0 0 26px rgba(30,34,44,.85)}
.nav{left:0;top:0;width:1200px;height:60px;background:rgba(20,30,60,.55)}
.brand{left:48px;top:18px;font-weight:900;font-size:20px;color:var(--white);letter-spacing:.5px}
.nav-links{left:420px;top:23px;display:flex;gap:28px;font-family:"Montserrat",sans-serif;font-weight:700;font-size:12px;color:var(--white);letter-spacing:.5px}
.social{display:flex;gap:14px}
.social span{width:16px;height:16px;border-radius:50%;background:currentColor;display:block}
.hero-social{left:1100px;top:22px;color:var(--white)}
.hero-arrow{left:1145px;top:312px}
/* headings */
.section-title{width:1200px;left:0;text-align:center;font-family:"Montserrat",sans-serif;font-weight:700;font-size:19px;color:var(--blue);letter-spacing:1px}
.section-sub{width:1200px;left:0;text-align:center;font-size:12px;color:var(--muted)}
/* features */
.feature{width:210px}
.feature h3{font-size:14px;font-weight:700;color:var(--ink);margin-bottom:6px;padding-left:46px}
.feature p{font-size:10.5px;line-height:1.55;color:var(--muted);padding-left:46px}
.feature svg{position:absolute;left:0;top:0}
/* solutions illustration area */
.solutions-art{left:90px;top:1010px;width:1020px;height:600px;background:radial-gradient(ellipse at 50% 50%,#eef0f4 0%,#f7f8fa 55%,#ffffff 100%)}
/* team */
.phone{width:262px;height:380px;border-radius:30px;background:var(--phone);padding:34px 14px 40px}
.phone-screen{width:100%;height:100%;border-radius:4px;overflow:hidden;position:relative}
.phone-name{text-align:center;font-family:"Montserrat",sans-serif;font-weight:700;font-size:17px;color:var(--white);padding-top:16px}
.phone-role{text-align:center;font-size:10px;color:var(--white);opacity:.9;margin-top:2px;text-transform:uppercase;letter-spacing:.5px}
.phone-photo{position:absolute;left:50%;top:88px;width:140px;height:140px;margin-left:-70px;border-radius:50%;border:5px solid var(--white)}
.badge{width:54px;height:54px;border-radius:50%;display:flex;align-items:center;justify-content:center;font-size:12px;font-weight:700;color:var(--white)}
.team-text{width:330px}
.team-text h3{font-family:"Montserrat",sans-serif;font-weight:700;font-size:19px;color:var(--blue);letter-spacing:.5px;margin:18px 0 12px}
.team-text p{font-size:14px;font-weight:700;line-height:1.6;color:var(--ink)}
.pills{display:flex;gap:6px;margin-top:16px}
.pills span{border:1px solid var(--line);border-radius:14px;padding:4px 10px;font-size:9px;color:var(--muted)}
/* articles */
.articles{left:0;top:3316px;width:1200px;height:651px;background:var(--blue-band)}
.articles-kicker{left:230px;top:3370px;font-size:10px;color:rgba(255,255,255,.7)}
.articles-title{left:230px;top:3400px;font-family:"Montserrat",sans-serif;font-size:32px;color:var(--white)}
.articles-lead{left:230px;top:3452px;width:260px;font-size:10px;line-height:1.5;color:rgba(255,255,255,.7)}
.btn-all{left:846px;top:3390px;width:120px;height:30px;border-radius:15px;background:var(--white);font-size:10px;color:var(--ink);text-align:center;line-height:30px}
.card{top:3547px;height:215px;background:var(--white);border-radius:4px;padding:22px 20px;overflow:hidden}
.card h4{font-size:15px;font-weight:700;color:var(--ink)}
.card .meta{font-size:9px;color:var(--muted);margin:4px 0 10px}
.card .rule{width:50px;height:2px;background:var(--line);margin-bottom:14px}
.card p{font-size:10.5px;line-height:1.6;color:var(--muted)}
.card .foot{position:absolute;bottom:20px;left:20px;right:20px;display:flex;justify-content:space-between;font-size:9px;color:var(--muted)}
.card .dot{width:16px;height:16px;border-radius:3px;display:block}
/* manager */
.manager-name{left:140px;top:4072px;font-family:"Montserrat",sans-serif;font-weight:700;font-size:29px;color:var(--navy);letter-spacing:1px;white-space:nowrap}
.manager-role{left:200px;top:4114px;font-family:"Montserrat",sans-serif;font-weight:600;font-size:15px;color:var(--navy);letter-spacing:2px}
.manager-bio{left:140px;top:4160px;width:250px;font-size:12px;line-height:1.6;color:var(--navy)}
.manager-photo{left:410px;top:3990px;width:400px;height:440px;background:radial-gradient(ellipse at 55% 45%,#c9dcef 0%,#9dbde0 45%,#ffffff 75%)}
.skills{left:820px;top:4100px;width:240px}
.skill{margin-bottom:36px}
.skill-label{font-family:"Montserrat",sans-serif;font-weight:700;font-size:10px;color:var(--navy);margin-bottom:6px}
.skill-track{height:5px;background:#dfe3ee}
.skill-fill{height:5px;background:var(--navy)}
/* help */
.help{left:0;top:4437px;width:1200px;height:291px;background:var(--blue-help)}
.help-title{left:232px;top:4512px;font-family:"Montserrat",sans-serif;font-weight:700;font-size:22px;color:var(--white)}
.help-text{left:232px;top:4548px;width:290px;font-size:12px;font-weight:700;line-height:1.45;color:var(--white)}
.store{top:4628px;width:100px;height:32px;border-radius:6px;background:#111}
.devices{left:580px;top:4445px;width:510px;height:283px;border-radius:8px;background:linear-gradient(180deg,#eef1f7,#c5ccdb)}
/* footer */
.footer{left:0;top:4728px;width:1200px;height:224px;background:var(--navy)}
.footer-brand{left:48px;top:4778px;font-weight:900;font-size:24px;color:var(--white)}
.footer-links{left:440px;top:4782px;display:flex;gap:48px;font-size:12px;color:var(--white)}
.footer-links span:first-child{font-weight:700}
.footer-social{left:872px;top:4782px;color:var(--white)}
.footer-contact{left:1002px;top:4768px;font-size:10px;line-height:1.6;color:rgba(255,255,255,.7)}
.copyright{left:0;top:4900px;width:1200px;text-align:center;font-size:10px;color:rgba(255,255,255,.5)}
</style>
</head>
<body>

<!-- hero -->
<div class="abs hero" role="img" aria-label="Photo of a hand holding a tablet on a wooden desk with coffee, earphones and notebook"></div>
<div class="abs hero-screen" role="img" aria-label="Tablet screen showing the company name"></div>
<div class="abs" style="left:300px;top:240px;width:600px;text-align:center;font-weight:900;font-size:44px;color:var(--navy)">Corelink Systems</div>
<div class="abs nav"></div>
<div class="abs brand">Corelink Systems</div>
<nav class="abs nav-links"><span>HOME</span><span>OUR SERVICES</span><span>ABOUT US</span><span>OUR TEAM</span><span>CONTACT</span><span>US SUPPORT</span></nav>
<div class="abs social hero-social"><span></span><span></span><span></span></div>
<svg class="abs hero-arrow" width="24" height="40" viewBox="0 0 24 40"><path d="M4 4 L20 20 L4 36" fill="none" stroke="#fff" stroke-width="3"/></svg>

<!-- complete package -->
<div class="abs section-title" style="top:672px">THE COMPLETE PACKAGE</div>
<div class="abs section-sub" style="top:704px">Only necessary</div>

<div class="abs feature" style="left:230px;top:795px">
  <svg width="34" height="34" viewBox="0 0 34 34"><path d="M6 12 L12 5 H22 L28 12 L17 29 Z M6 12 H28" fill="none" stroke="var(--orange)" stroke-width="2"/></svg>
  <h3>Vantor Programme</h3>
  <p>Licensing, setup and ongoing care for every desktop app your practice runs day to day.</p>
</div>
<div class="abs feature" style="left:476px;top:795px">
  <svg width="34" height="34" viewBox="0 0 34 34"><path d="M9 24 A6 6 0 0 1 10 12 A8 8 0 0 1 25 13 A5.5 5.5 0 0 1 25 24 Z" fill="none" stroke="var(--orange)" stroke-width="2"/></svg>
  <h3>Cloud</h3>
  <p>Secure hosted storage and backup so your records are safe and always within reach.</p>
</div>
<div class="abs feature" style="left:722px;top:795px">
  <svg width="34" height="34" viewBox="0 0 34 34"><rect x="6" y="6" width="22" height="22" rx="3" fill="none" stroke="var(--orange)" stroke-width="2"/><circle cx="17" cy="17" r="4" fill="none" stroke="var(--orange)" stroke-width="2"/></svg>
  <h3>Managed IT</h3>
  <p>Round the clock monitoring and support that keeps your whole network running smoothly.</p>
</div>

<!-- IT solutions -->
<div class="abs section-title" style="top:962px">IT SOLUTIONS</div>
<div class="abs solutions-art" role="img" aria-label="Illustration of software engineering services: web hosting, software, products, printers and scanners, finance, programming, solutions and copiers linked to a central heading"></div>

<!-- team -->
<div class="abs section-title" style="top:1660px">OUR TEAM</div>

<div class="abs phone" style="left:291px;top:1752px">
  <div class="phone-screen" style="background:linear-gradient(180deg,#5b8fe8 0%,#5b8fe8 45%,#e9eef8 45%)">
    <div class="phone-name">Dale Pritchard</div>
    <div class="phone-role">Senior Field Technician</div>
    <div class="phone-photo" role="img" aria-label="Portrait of the senior field technician" style="background:linear-gradient(180deg,#9fd0f0,#6aa7da)"></div>
  </div>
</div>
<div class="abs badge" style="left:526px;top:1862px;background:#f5d24a">12k</div>
<div class="abs badge" style="left:238px;top:1990px;background:#5b8fe8">12°</div>
<div class="abs team-text" style="left:579px;top:1815px">
  <svg width="48" height="24" viewBox="0 0 48 24"><path d="M2 16 H40 L46 10 M8 16 L14 6 H30 L36 16" fill="none" stroke="var(--blue)" stroke-width="1.5"/></svg>
  <h3>WHEN THE CLOUDS</h3>
  <p>Variable information on the air humidity, the feeling of the weather, and the ability to share this with your friends</p>
  <div class="pills"><span>HTML</span><span>UI</span><span>Web</span></div>
</div>

<div class="abs phone" style="left:664px;top:2208px">
  <div class="phone-screen" style="background:linear-gradient(180deg,#f0703a 0%,#f0703a 60%,#f7c08f 60%)">
    <div class="phone-name">OWEN CARRICK</div>
    <div class="phone-role">Engineering Specialist</div>
    <div class="phone-photo" role="img" aria-label="Portrait of the engineering specialist" style="background:linear-gradient(180deg,#dfe3ea,#9aa3b0)"></div>
  </div>
</div>
<div class="abs badge" style="left:900px;top:2288px;background:#f5d24a">7day</div>
<div class="abs badge" style="left:625px;top:2510px;background:var(--orange)">32°</div>
<div class="abs team-text" style="left:232px;top:2360px">
  <svg width="40" height="40" viewBox="0 0 40 40"><circle cx="20" cy="20" r="18" fill="none" stroke="var(--blue)" stroke-width="1.5"/></svg>
  <h3>WIRELESS EDGE</h3>
  <p>Sometimes the simplest things are the hardest to find. So we created a new line for everyday life. Sometimes the</p>
  <div class="pills"><span>HTML</span><span>UI</span><span>Web</span></div>
</div>

<div class="abs phone" style="left:288px;top:2850px">
  <div class="phone-screen" style="background:linear-gradient(180deg,#cfd8ec 0%,#cfd8ec 55%,#9fe3e0 55%)">
    <div class="phone-name" style="color:var(--navy)">MARA LINWOOD</div>
    <div class="phone-role" style="color:var(--navy)">Office Manager</div>
    <div class="phone-photo" role="img" aria-label="Portrait of the office manager" style="background:linear-gradient(180deg,#c98b63,#7a4b32)"></div>
  </div>
</div>
<div class="abs badge" style="left:530px;top:2960px;background:#f5d24a">3day</div>
<div class="abs badge" style="left:252px;top:3090px;background:#6f8fd6">8°</div>
<div class="abs team-text" style="left:612px;top:2900px">
  <svg width="48" height="24" viewBox="0 0 48 24"><path d="M2 16 H40 L46 10 M8 16 L14 6 H30 L36 16" fill="none" stroke="var(--blue)" stroke-width="1.5"/></svg>
  <h3>MICROWAVE LINKS</h3>
  <p>Sometimes the simplest things are the hardest to find. So we created a new line for everyday life. Sometimes the</p>
  <div class="pills"><span>HTML</span><span>UI</span><span>Web</span></div>
</div>

<!-- articles -->
<div class="abs articles"></div>
<div class="abs" style="left:585px;top:3300px;width:30px;height:30px;border-radius:50%;background:var(--white)"></div>
<div class="abs articles-kicker">Latest news</div>
<div class="abs articles-title">Recent articles</div>
<div class="abs articles-lead">Short reads on keeping clinics, practices and offices secure, fast and online.</div>
<div class="abs btn-all">View all articles</div>

<div class="abs card" style="left:-110px;width:335px">
  <p style="margin-top:62px;padding-left:110px">Plan upgrades early and keep every machine patched and backed up.</p>
  <div class="foot"><span></span><span class="dot" style="background:#6b5fd6"></span></div>
</div>
<div class="abs card" style="left:251px;width:331px">
  <h4>Data is all about the details</h4>
  <div class="meta">12 March 2024</div><div class="rule"></div>
  <p>Clean records and tidy backups make every audit easier and every restore faster.</p>
  <div class="foot"><span>5 comments</span><span class="dot" style="background:#f5c542"></span></div>
</div>
<div class="abs card" style="left:602px;width:358px;padding-left:150px">
  <div class="abs" role="img" aria-label="Photo of hands typing on a laptop" style="left:0;top:0;width:130px;height:215px;background:linear-gradient(180deg,#b9c2cc,#6f7884)"></div>
  <h4>Quality vs quantity</h4>
  <div class="meta">4 March 2024</div><div class="rule"></div>
  <p>Fewer, better tools often beat a crowded desktop full of apps.</p>
  <div class="foot" style="left:150px"><span>3 comments</span><span class="dot" style="background:#e86aa0"></span></div>
</div>
<div class="abs card" style="left:980px;width:250px">
  <h4>Time matters most</h4>
  <div class="meta">28 Feb 2024</div><div class="rule"></div>
  <p>Fast response keeps your patients seen and your staff working.</p>
  <div class="foot"><span>8 comments</span><span></span></div>
</div>

<!-- manager -->
<div class="abs manager-photo" role="img" aria-label="Photo of the manager in a blue shirt pointing to the side"></div>
<div class="abs manager-name">ETHAN MARLOW</div>
<div class="abs manager-role">MANAGER</div>
<div class="abs manager-bio">Lorem ipsum dolor sit amet, consectetur adipiscing elit, sed do eiusmod tempor incididunt ut labore et dolore magna aliqua. Ut enim ad minim veniam, quis nostrud exercitation ullamco laboris nisi.</div>
<div class="abs skills">
  <div class="skill"><div class="skill-label">DESKTOP SUPPORT – 24 YEARS</div><div class="skill-track"><div class="skill-fill" style="width:100%"></div></div></div>
  <div class="skill"><div class="skill-label">SERVER MANAGEMENT – 20 YEARS</div><div class="skill-track"><div class="skill-fill" style="width:84%"></div></div></div>
  <div class="skill"><div class="skill-label">SOFTWARE INSTALLATIONS – 14 YEARS</div><div class="skill-track"><div class="skill-fill" style="width:60%"></div></div></div>
  <div class="skill"><div class="skill-label">NETWORK – 12 YEARS</div><div class="skill-track"><div class="skill-fill" style="width:50%"></div></div></div>
</div>

<!-- get help -->
<div class="abs help"></div>
<div class="abs help-title">GET HELP</div>
<div class="abs help-text">Just download the app from the store. Simple, nice and user friendly application for help. Only relevant and useful information.</div>
<div class="abs store" style="left:232px"></div>
<div class="abs store" style="left:342px"></div>
<div class="abs devices" role="img" aria-label="Laptop, monitor, tablet and phone showing the support dashboard"></div>

<!-- footer -->
<div class="abs footer"></div>
<div class="abs footer-brand">Corelink Systems</div>
<div class="abs footer-links"><span>Home</span><span>Features</span><span>Reviews</span><span>Download</span></div>
<div class="abs social footer-social"><span></span><span></span><span></span></div>
<div class="abs footer-contact">(00) 5550 1234<br>hello@tvkb-example.net<br>www.tvkb-example.net<br>14 Harbour Lane, Suite 2<br>Open Mon–Fri 8am–6pm</div>
<div class="abs copyright">© 2024 Corelink Systems. All rights reserved.</div>

</body>
</html>
```